Business Card Design

Buy and sell properties
Buy and rehab properties
Buy properties for cash
That is what I do but do need a logo
looking for some type of logo or design on it
Just started business
Back of card should say something like BUY HOUSES CASH
Overview: it is a new company. Basically I buy properties wholesale and fix them up and sell them or sell them to other fix and flippers
Background: company is new so not any background
Market: is basically anyone selling a house or buying a house. Someone that needs to sell house fast. Basically I am a cash home buyer!!!

Updates
Email on card should be:   harborlanerealtyinc@mailbox.test

Industry/Entity Type
House
Contact Information for Business Card
Harbor Lane Realty Inc
PO Box 718269
Cedar Marsh FL 32987

Dale Morrick
harborlanerealtyinc@mailbox.test
555-271-6094

```html
<!DOCTYPE html>
<html lang="en">
<head>
<meta charset="utf-8">
<title>Harbor Lane Realty Inc — Business Card</title>
<link rel="stylesheet" href="https://fonts.googleapis.com/css2?family=Montserrat:wght@500;600;700&family=Questrial&display=swap">
<style>
  :root {
    --stage: #2e3033;
    --card: #ffffff;
    --ink: #3a3b3d;
    --ink-soft: #55575a;
    --rule: #4a4b4d;
    --brand-green: #2f9e48;
    --icon-blue: #2a3f9a;
  }
  * { box-sizing: border-box; margin: 0; padding: 0; }
  html, body {
    width: 1200px; height: 790px; overflow: hidden;
    background: var(--stage);
  }
  .stage { position: relative; width: 1200px; height: 790px; }

  .card {
    position: absolute;
    background: var(--card);
    box-shadow: 0 6px 18px rgba(0,0,0,.45);
  }

  .brand {
    position: absolute;
    display: flex; align-items: center; gap: 14px;
    white-space: nowrap;
  }
  .brand-mark {
    flex: none; border-radius: 50%;
    background: var(--brand-green);
  }
  .brand-name {
    font-family: "Montserrat", sans-serif;
    font-weight: 600;
    color: var(--ink);
    line-height: 1;
  }

  /* Back card */
  .card-back { left: 307px; top: 48px; width: 608px; height: 280px; }
  .card-back .brand { left: 0; right: 0; top: 95px; justify-content: center; }
  .card-back .brand-mark { width: 48px; height: 48px; }
  .card-back .brand-name { font-size: 36px; }
  .tagline-row {
    position: absolute; left: 0; right: 0; top: 236px;
    display: flex; align-items: center; gap: 12px;
  }
  .tagline-row .line { flex: 1; height: 1.5px; background: var(--rule); }
  .tagline {
    font-family: "Montserrat", sans-serif; font-weight: 700;
    font-size: 14px; letter-spacing: .5px; color: var(--ink);
  }

  /* Front card */
  .card-front { left: 520px; top: 380px; width: 640px; height: 340px; }
  .card-front .brand { left: 40px; top: 85px; }
  .card-front .brand-mark { width: 40px; height: 40px; }
  .card-front .brand-name { font-size: 27px; }
  .name-row {
    position: absolute; left: 40px; right: 40px; top: 175px;
    display: flex; align-items: center; gap: 12px;
  }
  .name-row .line { flex: 1; height: 1.5px; background: var(--rule); }
  .holder {
    font-family: "Montserrat", sans-serif; font-weight: 700;
    font-size: 18px; color: var(--ink);
  }
  .contact {
    position: absolute; left: 40px; top: 225px;
    border-top: 1.5px solid var(--rule); padding-top: 8px;
    font-family: "Questrial", sans-serif; font-size: 17px; color: var(--ink-soft);
    line-height: 1.3;
  }
  .contact li { list-style: none; display: flex; align-items: center; gap: 8px; white-space: nowrap; }
  .contact svg { width: 16px; height: 14px; flex: none; }
  .contact .company { font-family: "Montserrat", sans-serif; font-weight: 700; color: var(--ink); margin-top: 4px; }
  .contact .address { color: var(--ink); }

  /* Standalone logo panel */
  .logo-panel { left: 20px; top: 508px; width: 420px; height: 262px; box-shadow: none; }
  .logo-panel .brand { left: 0; right: 0; top: 110px; justify-content: center; }
  .logo-panel .brand-mark { width: 40px; height: 40px; }
  .logo-panel .brand-name { font-size: 28px; }
</style>
</head>
<body>
<main class="stage">

  <section class="card card-back" aria-label="Card back">
    <div class="brand"><span class="brand-mark"></span><span class="brand-name">Harbor Lane Realty Inc</span></div>
    <div class="tagline-row">
      <span class="line"></span>
      <span class="tagline">BUY HOUSES CASH</span>
      <span class="line"></span>
    </div>
  </section>

  <section class="card card-front" aria-label="Card front">
    <div class="brand"><span class="brand-mark"></span><span class="brand-name">Harbor Lane Realty Inc</span></div>
    <div class="name-row">
      <span class="line"></span>
      <span class="holder">Dale Morrick</span>
    </div>
    <ul class="contact">
      <li>
        <svg viewBox="0 0 16 14" aria-hidden="true"><path d="M2 5c0-2 2-3 6-3s6 1 6 3l-3 1-1-2H6L5 6z M4 7h8l2 6H2z" fill="var(--icon-blue)"/></svg>
        555-271-6094
      </li>
      <li>
        <svg viewBox="0 0 16 14" aria-hidden="true"><rect x="1" y="2" width="14" height="10" fill="var(--icon-blue)"/><path d="M1 2l7 6 7-6" stroke="#fff" stroke-width="1.2" fill="none"/></svg>
        harborlanerealtyinc@mailbox.test
      </li>
      <li class="company">Harbor Lane Realty Inc</li>
      <li class="address">PO Box 718269 Cedar Marsh FL</li>
    </ul>
  </section>

  <section class="card logo-panel" aria-label="Logo">
    <div class="brand"><span class="brand-mark"></span><span class="brand-name">Harbor Lane Realty Inc</span></div>
  </section>

</main>
</body>
</html>
```